Marlowe Tindra Pale Ale Beer Label/Badge

We need a Beer Label designed for our first official beer to be launched under The marlowe Brand!!
It will be a Pale Ale Called "Tindra Pale Ale"!

The Marlowe has the largest Craft Beer & Cider selection in the Geelong & Surf Coast region. With a funky location and a relaxed vibe, Marlowe prides itself on serving delicious, unique seasonal food paired with Australia's best Craft Beer. The marlowe is the perfect setting for a relaxed afternoon or evening with friends and can package an experience for larger groups or corporate bookings.

The Marlowe Tavern brand has been growing for over a year and a half and the first label needs to integrate The marlowe Logo but at the same time bring a fresh, new and eye catching feel to it along with embracing the "Odysseus" story in which we will be naming future beers.

The story of Tindra is found via the following link
http://en.lorevault.example/wiki/Tindra_(legend)

We expect designers to research The marlowe Tavern brand along with the all important Craft Beer Market and demographics. This will, potentially, be the start of many more labels to come for the winning designer!!

Requirements
Must have
• The original "O" needs to be integrated into the new logo and as much as the Greek mythology is being used it needs to be certain that this is an original Australian Craft Beer in the modern age!!
strong, modern & unique!!
Nice to have
• Logo could have a depiction of Tindra
Should not have
• tackiness or cheap!!

```html
<!DOCTYPE html>
<html lang="en">
<head>
<meta charset="utf-8">
<title>Marlowe Tindra Pale Ale – Label</title>
<link rel="stylesheet" href="https://fonts.googleapis.com/css2?family=Cinzel:wght@500;700&family=Cormorant+Garamond:ital,wght@1,500&display=swap">
<style>
  :root {
    --page: #ffffff;
    --cream: #f6efd9;
    --slate: #3f525b;
    --slate-dark: #2c3a41;
    --brick: #a86a5c;
    --brick-deep: #8a4f43;
    --brick-soft: #c4917f;
  }
  html, body {
    margin: 0;
    width: 1200px;
    height: 981px;
    overflow: hidden;
    background: var(--page);
  }
  .label {
    display: block;
    width: 1200px;
    height: 981px;
  }
  .label__ring-text {
    font-family: "Cinzel", serif;
    font-weight: 700;
    fill: var(--slate);
  }
  .label__place {
    font-family: "Cinzel", serif;
    font-weight: 500;
    fill: var(--slate);
  }
  .label__beer-name {
    font-family: "Cinzel", serif;
    font-weight: 700;
    fill: var(--cream);
  }
  .label__brand {
    font-family: "Cinzel", serif;
    font-weight: 700;
    fill: var(--cream);
  }
  .label__ribbon-text {
    font-family: "Cormorant Garamond", serif;
    font-style: italic;
    font-weight: 500;
    fill: var(--slate);
  }
</style>
</head>
<body>
<svg class="label" viewBox="0 0 1200 981" xmlns="http://www.w3.org/2000/svg" aria-label="Marlowe Tindra Pale Ale beer label">
  <defs>
    <path id="arc-top" d="M 385 490 A 215 300 0 0 1 815 490"/>
    <path id="arc-bottom" d="M 348 490 A 252 342 0 0 0 852 490"/>
    <path id="arc-name" d="M 440 470 A 160 228 0 0 0 760 470"/>
  </defs>

  <!-- outer badge -->
  <ellipse class="label__outline" cx="600" cy="490" rx="276" ry="371" fill="var(--slate)"/>
  <ellipse class="label__ring" cx="600" cy="490" rx="270" ry="365" fill="var(--cream)"/>

  <!-- side ribbons -->
  <g class="label__ribbon label__ribbon--left">
    <polygon points="300,470 262,462 278,495 262,528 300,520" fill="var(--slate-dark)"/>
    <rect x="298" y="462" width="130" height="58" fill="var(--cream)" stroke="var(--slate)" stroke-width="4"/>
    <text class="label__ribbon-text" x="358" y="497" font-size="15" text-anchor="middle">Handcrafted Beer</text>
  </g>
  <g class="label__ribbon label__ribbon--right">
    <polygon points="900,470 938,462 922,495 938,528 900,520" fill="var(--slate-dark)"/>
    <rect x="772" y="462" width="130" height="58" fill="var(--cream)" stroke="var(--slate)" stroke-width="4"/>
    <text class="label__ribbon-text" x="842" y="497" font-size="16" text-anchor="middle">ABV 5%</text>
  </g>

  <!-- inner medallion -->
  <ellipse class="label__medallion-edge" cx="600" cy="490" rx="196" ry="268" fill="var(--slate)"/>
  <ellipse class="label__medallion" cx="600" cy="490" rx="190" ry="262" fill="var(--brick)"/>
  <ellipse class="label__medallion-line" cx="600" cy="490" rx="178" ry="250" fill="none" stroke="var(--cream)" stroke-width="2"/>

  <!-- brand mark -->
  <g class="label__brand-mark">
    <circle cx="548" cy="268" r="8" fill="var(--cream)"/>
    <text class="label__brand" x="564" y="275" font-size="20">Marlowe</text>
  </g>

  <!-- illustration area -->
  <ellipse class="label__illustration" cx="600" cy="440" rx="130" ry="130" fill="var(--brick-soft)" role="img" aria-label="Cream profile illustration of Tindra with spiral hair, framed by wheat sprigs"/>

  <!-- ring text -->
  <text class="label__ring-text" font-size="40" letter-spacing="1">
    <textPath href="#arc-top" startOffset="50%" text-anchor="middle">MARLOWE TAVERN &amp; BREWERY</textPath>
  </text>
  <text class="label__place" font-size="26" letter-spacing="1">
    <textPath href="#arc-bottom" startOffset="50%" text-anchor="middle">MOUNT CALDER, VICTORIA, AUSTRALIA</textPath>
  </text>
  <text class="label__beer-name" font-size="34" letter-spacing="1">
    <textPath href="#arc-name" startOffset="50%" text-anchor="middle">TINDRA PALE ALE</textPath>
  </text>
</svg>
</body>
</html>
```